Online Advertising agency with fun music culture twist

We need a new website for our online advertising agency. The current site is just a placeholder but you can pull the text from the site- pebblebidhouse.com. The new site will be 10 total pages. The current site has 8 pages. So this project will require the design and code for all 10 pages.

Things I like- Clean, easy to read, custom graphics, video,
splash 1-2 colors, futuristic, music twist, fun, interesting, looks amazing on a mobile site, extremely professional design.

Things I don't like- I hate stock graphics, pages that scroll to much, to many colors (rainbow), sites that don't flow, very templated cookie cutter sites, not mobile compliant.

We built a sophisticated buying platform for advertisers to reach the right person on the right device at the right time. I used to be a concert promoter and I have several musicians that work with us. We want to play into the fun and excitement of live music with an advertising twist hence the name Pebble. We don't want to make it seem like a music company but we can use subtle vinyl and music references. My other company is marrowpixel.com for reference. I really like to design of my other company.

Target Market(s)

Online websites and fortune 500 advertisers- You can see my other company at marrowpixel.com

Industry/Entity Type

Advertising

Coding

Coded - Design and coding required

Number of Pages Required

5+ page

Font styles to use
Other font styles liked:
• Be creative

Requirements
Must have
• HTML5, Clean, easy to read, custom graphics, use of video graphics,
• splash 1-2 colors, futuristic, music twist, fun, interesting, looks amazing on a mobile site, extremely professional design. Play into the music theme, vinyl records etc
Nice to have
• Video, interactivity, custom build (not a template)
Should not have
• Flash. I hate stock photos, pages that scroll to much, to many colors (rainbow), sites that don't flow, very templated cookie cutter sites, not mobile compliant.

```html
<!DOCTYPE html>
<html lang="en">
<head>
<meta charset="utf-8">
<title>Pebble Trading Desk</title>
<link href="https://fonts.googleapis.com/css2?family=Raleway:wght@300;400;500;700;800&display=swap" rel="stylesheet">
<style>
:root{
  --black:#050505;
  --white:#ffffff;
  --band:#7c7c7c;
  --footer:#dcdcdc;
  --text:#1a1a1a;
  --muted:#707070;
  --ring:#d9d9d9;
  --field:#f2f2f2;
}
*{margin:0;padding:0;box-sizing:border-box}
html,body{width:890px;height:1200px;overflow:hidden}
body{font-family:'Raleway',sans-serif;background:var(--white);color:var(--text);position:relative}
.hero{position:absolute;left:0;top:0;width:890px;height:410px;
  background:radial-gradient(ellipse at 30% 60%,#6b5a45 0%,#3a3129 35%,#15120f 75%),#111}
.hero-photo{position:absolute;inset:0;background:linear-gradient(180deg,rgba(0,0,0,.85) 0%,rgba(0,0,0,.2) 30%,rgba(0,0,0,.25) 80%,rgba(0,0,0,.4) 100%)}
.brand{position:absolute;left:60px;top:14px;width:152px;text-align:center;color:#cfcfcf}
.brand-name{font-weight:700;font-size:34px;letter-spacing:3px;line-height:36px;text-transform:uppercase}
.brand-sub{font-size:9px;letter-spacing:2px;border-top:1px solid #aaa;margin-top:2px;padding-top:1px;text-transform:uppercase}
.nav{position:absolute;right:58px;top:29px;display:flex;gap:15px;list-style:none}
.nav li{color:var(--white);font-size:11px;font-weight:500}
.nav li.active{color:#bdbdbd}
.hero-title{position:absolute;left:0;right:0;top:160px;text-align:center;color:var(--white);
  font-weight:800;font-size:39px;line-height:53px;text-transform:uppercase}
.partners{position:absolute;left:0;top:410px;width:890px;height:122px;background:var(--band)}
.partners .notch{position:absolute;left:428px;top:0}
.partners h2{position:absolute;left:60px;top:24px;color:var(--white);font-weight:400;font-size:16px}
.partner-row{position:absolute;left:60px;right:58px;top:62px;display:flex;justify-content:space-between;align-items:center}
.partner{display:flex;align-items:center;gap:6px;color:var(--white);font-weight:500;font-size:20px}
.partner .dot{width:36px;height:36px;border-radius:50%;background:#d8d8d8}
.partner .box{width:14px;height:14px;background:#d8d8d8}
.features-title{position:absolute;left:0;right:0;top:584px;text-align:center;font-size:19px;font-weight:500}
.features-title::before,.features-title::after{content:"";display:inline-block;width:60px;height:2px;vertical-align:middle;margin:0 8px;
  background:linear-gradient(90deg,transparent,#222,transparent)}
.feature{position:absolute;top:649px;width:180px;text-align:center}
.feature .ring{width:106px;height:106px;margin:0 auto;border:2px solid var(--ring);border-radius:50%;display:flex;align-items:center;justify-content:center}
.feature h3{margin-top:22px;font-weight:400;font-size:14px;line-height:20px;text-transform:uppercase}
.feature p{margin-top:13px;font-weight:300;font-size:10px;line-height:16px;color:var(--muted)}
.newsletter{position:absolute;left:0;top:914px;width:716px;height:38px;background:var(--black);
  clip-path:polygon(0 0,696px 0,716px 100%,0 100%)}
.newsletter label{position:absolute;left:59px;top:12px;color:var(--white);font-size:11.5px}
.newsletter .field{position:absolute;top:9px;width:163px;height:21px;background:var(--field);font-size:8px;color:#888;padding:6px 6px}
.newsletter .send{position:absolute;left:549px;top:9px;width:71px;height:21px;background:#e4e4e4;font-size:11px;text-align:center;line-height:21px}
.social-square{position:absolute;top:922px;width:21px;height:21px;background:#4a4a4a}
.footer{position:absolute;left:0;top:952px;width:890px;height:208px;background:var(--footer)}
.contact{position:absolute;left:59px;top:40px;font-size:11px;line-height:16px}
.contact .email{margin-top:9px}
.circles{display:flex;gap:11px;margin-top:15px}
.circles span{width:18px;height:18px;border-radius:50%;background:var(--black)}
.about{position:absolute;left:264px;top:40px;width:448px}
.about h2{font-weight:400;font-size:15px}
.about p{margin-top:14px;font-weight:300;font-size:9.4px;line-height:16px;letter-spacing:-.1px;color:var(--muted)}
.footer-links{position:absolute;left:743px;top:40px;list-style:none;font-size:10px;line-height:20px;text-transform:uppercase}
.bottom{position:absolute;left:0;top:1160px;width:890px;height:40px;background:var(--black);color:var(--white)}
.bottom .copy{position:absolute;left:59px;top:15px;font-size:8px;text-transform:uppercase}
.bottom .policy{position:absolute;right:59px;top:14px;font-size:9.5px;text-transform:uppercase}
</style>
</head>
<body>
<header class="hero">
  <div class="hero-photo" role="img" aria-label="Close-up of a dimly lit audio mixing console with glowing coloured buttons"></div>
  <div class="brand"><div class="brand-name">Pebble</div><div class="brand-sub">Trading Desk</div></div>
  <ul class="nav">
    <li class="active">HOME</li><li>ABOUT US</li><li>WHY CHOOSE US</li><li>ADVERTISERS</li><li>PUBLISHERS</li><li>CONTACT US</li>
  </ul>
  <h1 class="hero-title">Advertising made easy<br>with a unified<br>buying platform</h1>
</header>

<section class="partners">
  <svg class="notch" width="34" height="28" viewBox="0 0 34 28"><polygon points="0,0 34,0 17,28" fill="#1a1a1a"/></svg>
  <h2>OUR PARTNERS:</h2>
  <div class="partner-row">
    <div class="partner">Marlow's <span class="dot"></span></div>
    <div class="partner">Ridgeline</div>
    <div class="partner">Lumen Home</div>
    <div class="partner"><span class="dot"></span></div>
    <div class="partner"><span class="box"></span>Northgate Lending</div>
  </div>
</section>

<h2 class="features-title">OUR FEATURES</h2>

<div class="feature" style="left:58px">
  <div class="ring"><svg width="68" height="48" viewBox="0 0 68 48" fill="none" stroke="#111" stroke-width="3"><rect x="2" y="2" width="44" height="30"/><rect x="34" y="14" width="30" height="26"/><rect x="6" y="26" width="12" height="20" fill="#fff"/><circle cx="24" cy="17" r="5" stroke-width="2"/></svg></div>
  <h3>Cross-channel<br>targeting</h3>
  <p>We'll help you reach viewers across devices through video, display, mobile and native ads.</p>
</div>
<div class="feature" style="left:256px">
  <div class="ring"><svg width="56" height="56" viewBox="0 0 56 56"><circle cx="12" cy="16" r="8" fill="none" stroke="#111" stroke-width="4" stroke-dasharray="3 2"/><circle cx="24" cy="6" r="4" fill="none" stroke="#111" stroke-width="2"/><circle cx="33" cy="34" r="14" fill="none" stroke="#111" stroke-width="7" stroke-dasharray="5 3"/></svg></div>
  <h3>Automated<br>buying</h3>
  <p>We'll help you reach viewers across devices through video, display, mobile and native ads.</p>
</div>
<div class="feature" style="left:454px">
  <div class="ring"><svg width="66" height="66" viewBox="0 0 66 66"><path d="M33 0a33 33 0 0 0 0 66z" fill="#000"/><path d="M33 0a33 33 0 0 1 0 66z" fill="#ddd"/></svg></div>
  <h3>Full<br>transparency</h3>
  <p>We'll help you reach viewers across devices through video, display, mobile and native ads.</p>
</div>
<div class="feature" style="left:652px">
  <div class="ring"><svg width="60" height="46" viewBox="0 0 60 46"><rect x="4" y="8" width="26" height="10" transform="rotate(40 17 13)" fill="#bbb"/><rect x="26" y="10" width="30" height="12" transform="rotate(-40 41 16)" fill="#111"/><rect x="14" y="24" width="22" height="10" transform="rotate(-40 25 29)" fill="#111"/></svg></div>
  <h3>True<br>partnerships</h3>
  <p>We'll help you reach viewers across devices through video, display, mobile and native ads.</p>
</div>

<div class="newsletter">
  <label>NEWSLETTER SIGN UP:</label>
  <div class="field" style="left:197px">NAME</div>
  <div class="field" style="left:373px">EMAIL ID</div>
  <div class="send">SEND</div>
</div>
<span class="social-square" style="left:754px" aria-label="Social link"></span>
<span class="social-square" style="left:782px" aria-label="Social link"></span>
<span class="social-square" style="left:811px" aria-label="Social link"></span>

<footer class="footer">
  <div class="contact">
    <p>418 Larkin Ave, Fairhaven,<br>CO 80321</p>
    <p class="email">E-mail: contact@pebblebidhouse.com</p>
    <div class="circles"><span></span><span></span><span></span><span></span></div>
  </div>
  <div class="about">
    <h2>ABOUT US</h2>
    <p>Pebblebidhouse.com is not in the business of collecting, using, or selling consumer data; however it does offer tools and technologies to advertisers and publishers that allow them to collect and use user data. This is done primarily to enable these buyers and sellers of online video-advertising space to try and ensure that the audience they desire sees their ads and that the advertising itself is delivered and the performance of the advertising can be analyzed. Types of data that may be used for this purpose range from behavioral or interest-related information to geographical or demographical user data.</p>
  </div>
  <ul class="footer-links">
    <li>Home</li><li>About us</li><li>Why choose us</li><li>Advertisers</li><li>Publishers</li><li>Contact us</li>
  </ul>
</footer>

<div class="bottom">
  <span class="copy">Copyright © Pebble Trading Desk. All rights reserved</span>
  <span class="policy">Privacy policy</span>
</div>
</body>
</html>
```